Visitenkarten-Design für italienisches Küchenschiff
Zielgruppe
Restaurantschiff Morvella
Aufgabenstellung
Wir sind ein italienische Küche Schiff auf der Binnenalster in Hamburg und wollen den schönen Blick und gerne auch die italienischen Farben widerspiegeln...ich brauche das einmal neutral für den normalen Gast....und würde das denn..wenn es denn gut wird...auch gerne individell mit m e i n e r Tel Nr und auch für meine führenden Mitarbeiter personalisieren...aber...zuerst natürlich das neutrale...dazu schicke ich die alte Karte mit dem auch alten Logo was nicht unbedingt verwendet werden muss...

```html
<!DOCTYPE html>
<html lang="de">
<head>
<meta charset="utf-8">
<title>Morvella – Visitenkarten</title>
<link href="https://fonts.googleapis.com/css2?family=Advent+Pro:wght@300;400&display=swap" rel="stylesheet">
<style>
  :root {
    --page-top: #ffffff;
    --stage: #4b4b4b;
    --card-warm: #403c3c;
    --card-neutral: #383838;
    --band: #333333;
    --ink: #a99a87;
    --ink-soft: #9c8f7e;
    --green: #009a57;
    --white: #ffffff;
    --red: #a6302f;
    --map-light: #e6dfd0;
    --map-dark: #b1a592;
    --mark-faint: #424242;
  }
  * { box-sizing: border-box; margin: 0; padding: 0; }
  html, body { width: 1149px; height: 1200px; overflow: hidden; }
  body {
    position: relative;
    background: var(--stage);
    font-family: "Advent Pro", "Arial Narrow", sans-serif;
    font-weight: 300;
    color: var(--ink);
  }
  .page-top { position: absolute; left: 0; top: 0; width: 1149px; height: 51px; background: var(--page-top); }

  .card {
    position: absolute; width: 489px; height: 314px;
    background: var(--card-warm);
    box-shadow: 4px 4px 6px rgba(0,0,0,.45);
    overflow: hidden;
  }
  .card--neutral { background: var(--card-neutral); }

  /* front */
  .tricolore-v { position: absolute; left: 0; top: 0; width: 14px; height: 100%;
    background: linear-gradient(to bottom, var(--green) 0 33.4%, var(--white) 33.4% 66.7%, var(--red) 66.7%); }
  .side-band { position: absolute; left: 14px; top: 0; width: 18px; height: 100%; background: var(--band); }
  .map { position: absolute; left: 32px; top: 0; width: 212px; height: 100%;
    background: linear-gradient(135deg, var(--map-light) 0 30%, var(--map-dark) 30% 72%, var(--map-light) 72%); }
  .front-text { position: absolute; left: 274px; top: 0; right: 10px; }
  .brand { position: absolute; top: 88px; left: 0; display: flex; align-items: center; gap: 8px;
    font-size: 36px; font-weight: 300; color: var(--ink); line-height: 1; white-space: nowrap; }
  .brand-dot { width: 12px; height: 12px; border-radius: 50%; background: var(--ink); }
  .tagline { position: absolute; top: 130px; left: 0; font-size: 16.5px; letter-spacing: 1.6px; white-space: nowrap; }
  .contact { position: absolute; top: 156px; left: 0; font-size: 15px; line-height: 19px; white-space: nowrap; }
  .contact .gap { height: 4px; }
  .contact .label { display: inline-block; width: 32px; }

  /* back */
  .photo { position: absolute; left: 21px; width: 202px; }
  .photo--cabin { top: 18px; height: 123px;
    background: linear-gradient(to bottom, #c08a54 0 14%, #4f7fa8 14% 48%, #a33030 48% 62%, #eeeae4 62%); }
  .photo--night { top: 156px; height: 120px;
    background: linear-gradient(to bottom, #8c6f86 0%, #4e3f4d 55%, #2a2530 68%, #6b6050 80%, #1d1c22 100%); }
  .back-text { position: absolute; left: 246px; top: 0; right: 0; }
  .heading { position: absolute; left: 0; font-size: 20px; white-space: nowrap; }
  .line { position: absolute; left: 0; font-size: 15.5px; white-space: nowrap; }
  .hours .time { margin-left: 16px; }
  .divider { position: absolute; left: 43px; top: 145px; width: 117px; height: 1px; background: var(--ink-soft); }
  .tricolore-h { position: absolute; top: 287px; height: 9px;
    background: linear-gradient(to right, var(--green) 0 33.4%, var(--white) 33.4% 66.7%, var(--red) 66.7%); }

  .mark-large { position: absolute; left: 321px; top: 1010px; font-size: 110px; font-weight: 300;
    color: var(--mark-faint); line-height: 1; white-space: nowrap; }
</style>
</head>
<body>
  <div class="page-top"></div>

  <!-- Row 1 -->
  <section class="card card--front" style="left:58px; top:86px;">
    <div class="tricolore-v"></div>
    <div class="side-band"></div>
    <div class="map" role="img" aria-label="Lageplan an der Binnenalster mit Markierung des Anlegers"></div>
    <div class="front-text">
      <div class="brand"><span>Morvella</span><span class="brand-dot"></span></div>
      <div class="tagline">Schiffsrestaurant Morvella</div>
      <div class="contact">
        <div>Seeufer 14 (Wasserseite)</div>
        <div>20095 Hamburg</div>
        <div class="gap"></div>
        <div>Kontakt</div>
        <div><span class="label">Tel:</span> +49 040 / 55 01 23</div>
        <div><span class="label">Fax:</span> +49 040 / 55 01 24</div>
        <div>www.seeschiff-morvella.com</div>
        <div>E. info@seeschiff-morvella.com</div>
      </div>
    </div>
  </section>

  <section class="card card--back" style="left:602px; top:86px;">
    <div class="photo photo--cabin" role="img" aria-label="Gedeckte Tische im Salon des Schiffs mit Blick auf die Alster"></div>
    <div class="photo photo--night" role="img" aria-label="Nächtliche Uferpromenade mit Lichtern, die sich im Wasser spiegeln"></div>
    <div class="back-text">
      <div class="heading" style="top:42px;">Öffnungszeiten</div>
      <div class="line hours" style="top:70px;">Montag - Sonntag <span class="time">12:00 - 23:00</span></div>
      <div class="line" style="top:94px; left:109px;">Küche bis 22:00</div>
      <div class="divider"></div>
      <div class="heading" style="top:169px;">Reservierungen</div>
      <div class="line" style="top:197px;">Wollen Sie einen Tisch reservieren? Wir</div>
      <div class="line" style="top:217px;">freuen uns auf Ihren Anruf oder eine:</div>
      <div class="line" style="top:237px;">reservierung@seeschiff-morvella.com</div>
    </div>
    <div class="tricolore-h" style="left:21px; width:468px;"></div>
  </section>

  <!-- Row 2 -->
  <section class="card card--front card--neutral" style="left:65px; top:468px;">
    <div class="tricolore-v"></div>
    <div class="side-band"></div>
    <div class="map" role="img" aria-label="Lageplan an der Binnenalster mit Markierung des Anlegers"></div>
    <div class="front-text">
      <div class="brand"><span>Morvella</span><span class="brand-dot"></span></div>
      <div class="tagline">Schiffsrestaurant Morvella</div>
      <div class="contact">
        <div>Seeufer 14 (Wasserseite)</div>
        <div>20095 Hamburg</div>
        <div class="gap"></div>
        <div>Kontakt</div>
        <div><span class="label">Tel:</span> +49 040 / 55 01 23</div>
        <div><span class="label">Fax:</span> +49 040 / 55 01 24</div>
        <div>www.seeschiff-morvella.com</div>
        <div>E. info@seeschiff-morvella.com</div>
      </div>
    </div>
  </section>

  <section class="card card--back card--neutral" style="left:608px; top:468px;">
    <div class="photo photo--cabin" role="img" aria-label="Gedeckte Tische im Salon des Schiffs mit Blick auf die Alster"></div>
    <div class="photo photo--night" role="img" aria-label="Nächtliche Uferpromenade mit Lichtern, die sich im Wasser spiegeln"></div>
    <div class="back-text">
      <div class="heading" style="top:42px;">Öffnungszeiten</div>
      <div class="line hours" style="top:70px;">Montag - Sonntag <span class="time">12:00 - 23:00</span></div>
      <div class="line" style="top:94px; left:109px;">Küche bis 22:00</div>
      <div class="divider"></div>
      <div class="heading" style="top:169px;">Reservierungen</div>
      <div class="line" style="top:197px;">Wollen Sie einen Tisch reservieren? Wir</div>
      <div class="line" style="top:217px;">freuen uns auf Ihren Anruf oder eine:</div>
      <div class="line" style="top:237px;">reservierung@seeschiff-morvella.com</div>
    </div>
    <div class="tricolore-h" style="left:0; width:489px;"></div>
  </section>

  <!-- Large brand mark -->
  <div class="mark-large">Morvella</div>
</body>
</html>
```